Email Marketing for HR and Career Consulting Company

I am looking for a email marketing template that will be developed in HTML format. Right now, we need PSD file format.

The content will include:

1. Featured / Poplar Blog post
2. Latest blog post this week
3. Latest jobs this week
4. Connect with us (social media)

This is a bi-weekly template which we will be sending to people who sign up our weekly newsletter. The purpose of the newsletter is to provide career advise and also latest jobs that's available from our company so that we can redirect them to our career page or apply to our latest jobs.
Updates

Project Deadline Extended
Reason: I am extending this deadline as I would like to see more designs. So far, I have only shortlisted one design that is close to what I am looking for. To all designers, please note that your design would have to be practical and easy to navigate. It also must take into consideration that when we develop this into html, it will b responsive.

Target Market(s)

Job seekers - age group 25 - 45

Industry/Entity Type

Consulting

Font styles to use
Other font styles liked:
• Helvetical

Colors
0492cd
e34197
ec1f27
85cae6
33a6d7
85acd3
eda3c7
e667a6
f59195

Requirements
Must have
• 1. Social media icons
• 2. Links - jobs, contact us
• 3. Popular career advice
• 4. Latest career advice
• 5. Featured jobs
• 6. Popular jobs
Nice to have
• I would like to see clean and minimalist design. Please try to avoid black color. Use pastel colors as much as possible. Our website is www.careerpondly.com.sg
Should not have
• Should avoid black and dark colors

```html
<!DOCTYPE html>
<html lang="en">
<head>
<meta charset="utf-8">
<title>Career Pondly Newsletter</title>
<link href="https://fonts.googleapis.com/css2?family=Open+Sans:wght@400;600;700&display=swap" rel="stylesheet">
<style>
  :root {
    --page-bg: #e6e9ec;
    --sheet: #f7f7f7;
    --header-bg: #ffffff;
    --band: #1493d0;
    --button: #33a6d7;
    --pink: #e3449a;
    --social: #9a8fb5;
    --social-foot: #b2388a;
    --bullet: #ec1f27;
    --ink: #2b2b2b;
    --muted: #6a6a6a;
    --nav: #6d6d6d;
    --white: #ffffff;
  }
  * { box-sizing: border-box; margin: 0; padding: 0; }
  html, body { width: 960px; height: 1200px; overflow: hidden; }
  body { background: var(--page-bg); font-family: "Open Sans", Arial, sans-serif; position: relative; }

  .newsletter {
    position: absolute; left: 252px; top: 62px;
    width: 570px; height: 1412px;
    transform: scale(0.8); transform-origin: top left;
    background: var(--sheet);
  }
  .abs { position: absolute; }
  .newsletter > section, .newsletter > header, .newsletter > footer, .newsletter > .band {
    position: absolute; left: 0; width: 570px;
  }

  .masthead { top: 0; height: 128px; background: var(--header-bg); }
  .main-nav { left: 30px; top: 46px; display: flex; gap: 31px; font-size: 13px; color: var(--nav); }
  .brand { left: 200px; top: 16px; width: 170px; text-align: center; }
  .brand-dot { width: 66px; height: 66px; border-radius: 50%; background: var(--band); margin: 0 auto; }
  .brand-name { font-size: 18px; font-weight: 600; color: #3a3a3a; margin-top: 6px; line-height: 1; }
  .social { display: flex; gap: 15px; }
  .social span { width: 38px; height: 38px; border-radius: 50%; background: var(--social); display: block; }
  .masthead .social { left: 394px; top: 36px; }

  .band {
    height: 46px; background: var(--band); color: var(--white);
    font-size: 15.5px; font-weight: 700; text-transform: uppercase;
    display: flex; align-items: center; justify-content: center; letter-spacing: 0.1px;
  }
  .band-advice { top: 128px; }
  .band-featured { top: 426px; }
  .band-hot { top: 735px; }
  .band-blog { top: 1042px; }

  .post-title { font-size: 16.5px; line-height: 24px; color: var(--ink); font-weight: 400; }
  .post-text { font-size: 12px; line-height: 19px; color: var(--muted); }
  .btn {
    width: 154px; height: 40px; border-radius: 20px; background: var(--button);
    color: var(--white); font-size: 13.5px; font-weight: 600;
    display: flex; align-items: center; justify-content: center;
  }

  .advice { top: 174px; height: 252px; }
  .advice .post-title { left: 30px; top: 20px; width: 250px; }
  .advice .post-text { left: 32px; top: 82px; width: 232px; }
  .advice .btn { left: 28px; top: 174px; }
  .advice .photo { left: 294px; top: 19px; width: 264px; height: 208px;
    background: linear-gradient(135deg, #5a86b8 0%, #dfe8f2 45%, #ffffff 60%, #a7bfd8 100%); }

  .featured { top: 472px; height: 263px; }
  .featured .photo { left: 13px; top: 14px; width: 272px; height: 214px;
    background: linear-gradient(160deg, #e9e6e3 0%, #f3efec 50%, #d9c2ae 100%); }
  .featured .post-title { left: 305px; top: 16px; width: 235px; text-align: center; }
  .featured .post-text { left: 310px; top: 75px; width: 232px; }
  .featured .btn { left: 344px; top: 186px; }

  .hot-jobs { top: 781px; height: 261px; }
  .job-list { left: 38px; top: 28px; list-style: none; }
  .job-list li { display: flex; align-items: center; font-size: 16.5px; color: var(--ink); height: 24px; }
  .job-list li::before { content: ""; width: 7px; height: 7px; background: var(--bullet); margin-right: 16px; flex: none; }
  .job-list a { color: var(--ink); text-decoration: underline; text-underline-offset: 3px; }
  .job-list li + li { margin-top: 12px; }
  .job-list li:nth-child(3) { margin-top: 9px; }
  .hot-jobs .btn { left: 202px; top: 195px; }

  .blog { top: 1088px; height: 267px; }
  .blog-grid { left: 17px; top: 30px; display: flex; gap: 16px; }
  .blog-card { width: 96px; }
  .thumb { width: 91px; height: 57px; }
  .blog-card p { font-size: 10.5px; line-height: 19px; color: var(--muted); margin-top: 5px; letter-spacing: -0.1px; }
  .t1 { background: linear-gradient(160deg, #eae7e4, #d9c2ae); }
  .t2 { background: linear-gradient(135deg, #e9a13b, #c64fa6, #4fb3d9); }
  .t3 { background: linear-gradient(180deg, #2b3036, #0e1114); }
  .t4 { background: linear-gradient(180deg, #a9d4d6, #e8efe8); }
  .t5 { background: linear-gradient(135deg, #e0844a, #cf6a35); }
  .blog .btn { left: 206px; top: 195px; }

  .site-footer { top: 1355px; height: 57px; background: var(--pink); }
  .site-footer .copy { left: 28px; top: 19px; font-size: 12.5px; color: var(--white); }
  .site-footer .social { left: 394px; top: 9px; }
  .site-footer .social span { background: var(--social-foot); }
</style>
</head>
<body>
<main class="newsletter">
  <header class="masthead">
    <nav class="main-nav abs"><span>Home</span><span>Jobs</span><span>Contact</span></nav>
    <div class="brand abs">
      <div class="brand-dot"></div>
      <div class="brand-name">careerpondly</div>
    </div>
    <div class="social abs">
      <span aria-label="Social link one"></span><span aria-label="Social link two"></span><span aria-label="Social link three"></span>
    </div>
  </header>

  <div class="band band-advice">Career Advice (Featured Post)</div>
  <section class="advice">
    <h2 class="post-title abs">Contract Jobs: Can They Really Be A Career Option?</h2>
    <p class="post-text abs">Last month, Career Pondly teamed up with Meridlink to tackle one of the industry's biggest questions: can you make a career out of contract jobs?</p>
    <a class="btn abs">Read More</a>
    <div class="photo abs" role="img" aria-label="Hand using a tablet showing a job search sketch"></div>
  </section>

  <div class="band band-featured">Featured Jobs (Job of the Week)</div>
  <section class="featured">
    <div class="photo abs" role="img" aria-label="Hands typing on a laptop on a wooden desk"></div>
    <h2 class="post-title abs">IT Service Desk Analyst<br>6-Months Contract)</h2>
    <p class="post-text abs">Our client, an Asia Pacific (APAC) Region office is hiring a Contract- IT Service Desk Analysts into their business encompassing 12 Countries and 31 offices.</p>
    <a class="btn abs">Apply Now</a>
  </section>

  <div class="band band-hot">Hot Jobs This Week</div>
  <section class="hot-jobs">
    <ul class="job-list abs">
      <li><a>Senior / Recruitment Consultant - Executive Search Division</a></li>
      <li><a>IT Service Desk Analyst 6-Months Contract)</a></li>
      <li><a>Logistics Manager - Fashion Retail</a></li>
      <li><a>Manager, Tender Analysis and Pricing Management, APAC</a></li>
    </ul>
    <a class="btn abs">Find more jobs</a>
  </section>

  <div class="band band-blog">Latest Blog Posts for the Week</div>
  <section class="blog">
    <div class="blog-grid abs">
      <article class="blog-card"><div class="thumb t1" role="img" aria-label="Laptop on a desk"></div><p>Your Digital Foot-print Part 5: The 21st Century Resume</p></article>
      <article class="blog-card"><div class="thumb t2" role="img" aria-label="Colourful gears illustration"></div><p>Defining Your Career: Chapter Two</p></article>
      <article class="blog-card"><div class="thumb t3" role="img" aria-label="Dark cinematic scene"></div><p>Life As An External Recruiter.Welcome to The Dark Side?</p></article>
      <article class="blog-card"><div class="thumb t4" role="img" aria-label="Illustration of someone leaving an office"></div><p>10 Things to Expect After You have Quit Your Job</p></article>
      <article class="blog-card"><div class="thumb t5" role="img" aria-label="Illustration of a ringing phone"></div><p>8 Reasons You're Not Getting Phone Calls During Your Job Search</p></article>
    </div>
    <a class="btn abs">Read More</a>
  </section>

  <footer class="site-footer">
    <p class="copy abs">© CareerPondly 2016 All rights reserved.</p>
    <div class="social abs">
      <span aria-label="Social link one"></span><span aria-label="Social link two"></span><span aria-label="Social link three"></span>
    </div>
  </footer>
</main>
</body>
</html>
```